Home Equity Lines of Credit
are BACK!!!

* Up to 97.5% on Owner Occupied Properties
* 700 Minimum Scores
* Fund in only 2-3 weeks

Can be used for...
* Education Expense
* Bill Consolidation
* Home Improvement
* Investments

Call today for more information!
(800) 647-2915

Bluecrest Lending Partners, Inc.
NMLS #318660
www.bluecrestlendhub.com

```html
<!DOCTYPE html>
<html lang="en">
<head>
<meta charset="utf-8">
<title>Home Equity Lines of Credit</title>
<link href="https://fonts.googleapis.com/css2?family=Oswald:wght@700&family=Lato:wght@400;700;900&display=swap" rel="stylesheet">
<style>
  :root {
    --blue: #0a5ea8;
    --blue-band: #1f7cc4;
    --blue-band-edge: #0b64ad;
    --gold: #d6cb93;
    --gold-dark: #b9a86a;
    --ink: #111111;
    --white: #ffffff;
  }
  * { box-sizing: border-box; margin: 0; padding: 0; }
  html, body { width: 1200px; height: 1200px; overflow: hidden; background: var(--white); }
  .ad {
    position: relative; width: 1200px; height: 1200px; overflow: hidden;
    background: var(--white); font-family: "Lato", sans-serif; color: var(--ink);
  }
  .hero-photo {
    position: absolute; left: 480px; top: 0; width: 720px; height: 613px;
    background:
      linear-gradient(90deg, #ffffff 0%, rgba(255,255,255,0.6) 30%, rgba(255,255,255,0) 60%),
      linear-gradient(180deg, #f2ece6 0%, #d9c5b5 35%, #8b93a8 70%, #3d4660 100%);
  }
  .headline { position: absolute; left: 48px; top: 52px; font-family: "Oswald", sans-serif; font-weight: 700; text-transform: uppercase; line-height: 1; }
  .headline .line-one { display: block; color: var(--blue); font-size: 94px; letter-spacing: 0.5px; }
  .headline .line-two { display: block; color: var(--gold); font-size: 75px; margin-top: 16px; letter-spacing: 0.5px; }
  .features { position: absolute; left: 46px; top: 270px; list-style: none; }
  .features li { display: flex; align-items: flex-start; font-size: 34px; line-height: 42px; margin-bottom: 28px; }
  .features li:nth-child(2) { margin-bottom: 28px; }
  .features .tick { width: 42px; height: 34px; margin-right: 10px; margin-top: 4px; flex: none; }
  .features em { font-style: normal; color: var(--blue); }
  .uses-tab {
    position: absolute; left: 379px; top: 549px; width: 452px; height: 65px;
    border-radius: 80px 80px 0 0;
    background: linear-gradient(180deg, var(--gold) 0%, var(--gold-dark) 100%);
    text-align: center; font-weight: 700; font-size: 33px; line-height: 76px;
  }
  .uses-band {
    position: absolute; left: 0; top: 613px; width: 1200px; height: 222px;
    background: linear-gradient(90deg, var(--blue-band-edge) 0%, var(--blue-band) 50%, var(--blue-band-edge) 100%);
  }
  .use { position: absolute; top: 32px; width: 280px; margin-left: -140px; text-align: center; color: var(--white); font-size: 27px; }
  .use .badge { display: block; margin: 0 auto 22px; width: 94px; height: 94px; border-radius: 50%; background: var(--white); box-shadow: 0 4px 10px rgba(0,0,0,0.2); }
  .use .badge svg { width: 94px; height: 94px; }
  .footer-photo {
    position: absolute; left: 0; top: 835px; width: 1200px; height: 365px;
    background: linear-gradient(90deg, #f6f6f7 0%, #ececee 40%, #f4f4f5 70%, #fafafa 100%);
  }
  .cta { position: absolute; left: 58px; top: 855px; color: var(--blue); font-weight: 900; text-transform: uppercase; line-height: 1; }
  .cta .big { display: block; font-size: 51px; }
  .cta .small { display: block; font-size: 37px; margin-top: 10px; }
  .phone { position: absolute; left: 59px; top: 955px; display: flex; align-items: center; color: var(--gold); font-size: 47px; font-weight: 700; }
  .phone svg { width: 52px; height: 52px; margin-right: 12px; }
  .company { position: absolute; left: 63px; top: 1050px; font-size: 27px; line-height: 33px; }
  .company .web { display: flex; align-items: center; margin-left: -4px; margin-top: 3px; }
  .company .web svg { width: 28px; height: 28px; margin-right: 10px; }
  .brand-mark { position: absolute; left: 690px; top: 960px; display: flex; align-items: center; }
  .brand-mark .dot { width: 70px; height: 70px; border-radius: 50%; background: var(--blue); margin-right: 16px; flex: none; }
  .brand-mark .name { font-size: 32px; font-weight: 700; color: var(--blue); line-height: 1.15; }
</style>
</head>
<body>
<div class="ad">
  <div class="hero-photo" role="img" aria-label="Photo of a worried couple sitting together reviewing household bills"></div>

  <h1 class="headline">
    <span class="line-one">Home Equity Lines</span>
    <span class="line-two">of Credit are Back !!!</span>
  </h1>

  <ul class="features">
    <li><svg class="tick" viewBox="0 0 42 34"><rect x="2" y="10" width="26" height="22" fill="none" stroke="#0a5ea8" stroke-width="3"/><path d="M9 18 L17 26 L40 3" fill="none" stroke="#0a5ea8" stroke-width="5" stroke-linecap="round"/></svg><span>Up to <em>97.5%</em> on Owner<br>Occupied Properties</span></li>
    <li><svg class="tick" viewBox="0 0 42 34"><rect x="2" y="10" width="26" height="22" fill="none" stroke="#0a5ea8" stroke-width="3"/><path d="M9 18 L17 26 L40 3" fill="none" stroke="#0a5ea8" stroke-width="5" stroke-linecap="round"/></svg><span><em>700</em> Minimum Scores</span></li>
    <li><svg class="tick" viewBox="0 0 42 34"><rect x="2" y="10" width="26" height="22" fill="none" stroke="#0a5ea8" stroke-width="3"/><path d="M9 18 L17 26 L40 3" fill="none" stroke="#0a5ea8" stroke-width="5" stroke-linecap="round"/></svg><span>Fund in only <em>2-3 weeks</em></span></li>
  </ul>

  <div class="uses-tab">Can be used for...</div>

  <section class="uses-band">
    <div class="use" style="left:164px">
      <span class="badge"><svg viewBox="0 0 94 94"><path d="M14 40 L47 28 L80 40 L47 52 Z" fill="#c9b56f"/><path d="M28 46 V62 Q47 70 66 62 V46 L47 54 Z" fill="#c9b56f"/><rect x="18" y="46" width="4" height="18" fill="#c9b56f"/></svg></span>
      Education Expense
    </div>
    <div class="use" style="left:464px">
      <span class="badge"><svg viewBox="0 0 94 94"><rect x="30" y="22" width="34" height="50" fill="none" stroke="#c9b56f" stroke-width="2.5"/><line x1="36" y1="58" x2="58" y2="58" stroke="#c9b56f" stroke-width="2.5"/><line x1="36" y1="64" x2="52" y2="64" stroke="#c9b56f" stroke-width="2.5"/><text x="36" y="46" font-size="16" font-family="Lato, sans-serif" fill="#c9b56f">$</text></svg></span>
      Bill Consolidation
    </div>
    <div class="use" style="left:748px">
      <span class="badge"><svg viewBox="0 0 94 94"><path d="M20 46 L47 22 L74 46 M28 40 V70 H66 V40" fill="none" stroke="#c9b56f" stroke-width="2.5"/><line x1="40" y1="48" x2="56" y2="64" stroke="#c9b56f" stroke-width="4" stroke-linecap="round"/></svg></span>
      Home Improvement
    </div>
    <div class="use" style="left:1030px">
      <span class="badge"><svg viewBox="0 0 94 94"><path d="M26 48 Q20 70 36 70 Q50 70 44 48 Z" fill="none" stroke="#c9b56f" stroke-width="2.5"/><text x="30" y="66" font-size="15" font-family="Lato, sans-serif" fill="#c9b56f">$</text><path d="M52 46 H72 L68 70 H56 Z" fill="none" stroke="#c9b56f" stroke-width="2.5"/><path d="M62 46 V28 M62 36 Q54 30 56 24 M62 32 Q70 26 70 20" fill="none" stroke="#c9b56f" stroke-width="2.5"/></svg></span>
      Investments
    </div>
  </section>

  <div class="footer-photo" role="img" aria-label="Faded photo of a relieved couple in the background"></div>

  <div class="cta">
    <span class="big">Call Today For</span>
    <span class="small">More Information !</span>
  </div>

  <div class="phone">
    <svg viewBox="0 0 52 52"><circle cx="26" cy="26" r="23" fill="none" stroke="#0a5ea8" stroke-width="3"/><path d="M18 15 L23 14 L25 21 L21 23 Q24 29 29 32 L31 28 L38 30 L37 35 Q33 39 27 36 Q18 31 15 22 Q14 18 18 15 Z" fill="#0a5ea8"/></svg>
    (800) 647-2915
  </div>

  <div class="company">
    <div>Bluecrest Lending Partners, Inc.</div>
    <div>NMLS #318660</div>
    <div class="web"><svg viewBox="0 0 28 28"><circle cx="14" cy="14" r="11" fill="none" stroke="#0a5ea8" stroke-width="2"/><ellipse cx="14" cy="14" rx="5" ry="11" fill="none" stroke="#0a5ea8" stroke-width="2"/><line x1="3" y1="14" x2="25" y2="14" stroke="#0a5ea8" stroke-width="2"/></svg>www.bluecrestlendhub.com</div>
  </div>

  <div class="brand-mark">
    <span class="dot"></span>
    <span class="name">Bluecrest Lending<br>Partners, Inc.</span>
  </div>
</div>
</body>
</html>
```